Book cover for book titled The Quiet Harbor's Drift Ledger

Need a book cover for a book size 5.25 x 8.
Title: The Quiet Harbor's Drift Ledger
Subtitle: 40 Habits You Might Shed on the Road to a Calmer Year in the Season of Change
Author: Dr. Marvin T. Okafor
Foreword by Leopold Vantrease, Ph.D.
The book cover should be white. I have uploaded 2 photos. The closeup with the hat should go on the front with the text. The one in the chair should go on the back. It will be the only thing on the back.

```html
<!DOCTYPE html>
<html lang="en">
<head>
<meta charset="utf-8">
<title>The Quiet Harbor's Drift Ledger — Cover</title>
<link href="https://fonts.googleapis.com/css2?family=Anton&family=Bebas+Neue&family=Barlow+Semi+Condensed:wght@300;400;500;600;700&display=swap" rel="stylesheet">
<style>
  :root {
    --ink: #1d1d1f;
    --ink-light: #2b2b2e;
    --amber: #f8ae3f;
    --white: #ffffff;
    --band: #58585a;
    --muted: #6e6e70;
    --photo-dark: #1a1a1a;
    --photo-mid: #3c3a38;
  }
  html, body {
    margin: 0;
    padding: 0;
    width: 787px;
    height: 1200px;
    overflow: hidden;
    background: var(--ink);
  }
  .cover {
    position: relative;
    width: 787px;
    height: 1200px;
    overflow: hidden;
    background: radial-gradient(ellipse at 50% 60%, var(--ink-light) 0%, var(--ink) 70%);
    font-family: "Barlow Semi Condensed", "Arial Narrow", sans-serif;
  }
  .cover-art {
    position: absolute;
    inset: 0;
    width: 787px;
    height: 1200px;
  }
  .title-block {
    position: absolute;
    left: 0;
    right: 0;
    top: 692px;
    text-align: center;
  }
  .title-kicker {
    margin: 0;
    font-family: "Bebas Neue", "Oswald", sans-serif;
    font-weight: 400;
    font-size: 64px;
    line-height: 1;
    color: var(--amber);
    letter-spacing: 0;
  }
  .title-main {
    margin: 6px 0 0;
    font-family: "Anton", "Impact", sans-serif;
    font-weight: 400;
    font-size: 124px;
    line-height: 1;
    color: var(--white);
    letter-spacing: -1px;
  }
  .subtitle {
    position: absolute;
    left: 0;
    right: 0;
    top: 898px;
    text-align: center;
  }
  .subtitle-count {
    display: flex;
    align-items: center;
    justify-content: center;
    gap: 10px;
    margin: 0;
    font-weight: 700;
    font-size: 27px;
    line-height: 1.2;
    color: var(--amber);
  }
  .subtitle-count::before,
  .subtitle-count::after {
    content: "";
    display: block;
    width: 174px;
    height: 1.5px;
    background: var(--white);
  }
  .subtitle-line {
    margin: 2px 0 0;
    font-weight: 300;
    font-size: 24px;
    line-height: 1.25;
    color: var(--amber);
  }
  .subtitle-tail {
    margin: 4px 0 0;
    font-weight: 400;
    font-size: 22px;
    line-height: 1.25;
    color: var(--white);
  }
  .subtitle-tail strong {
    font-weight: 700;
    font-size: 25px;
  }
  .author-band {
    position: absolute;
    left: 0;
    right: 0;
    top: 1079px;
    height: 46px;
    background: var(--band);
    display: flex;
    align-items: center;
    justify-content: center;
  }
  .author-name {
    margin: 0;
    font-weight: 500;
    font-size: 28px;
    color: var(--white);
  }
  .foreword {
    position: absolute;
    left: 0;
    right: 0;
    top: 1137px;
    margin: 0;
    text-align: center;
    color: var(--muted);
    font-weight: 400;
    font-size: 15px;
  }
  .foreword-name {
    font-size: 21px;
    font-weight: 500;
  }
</style>
</head>
<body>
  <main class="cover">
    <svg class="cover-art" viewBox="0 0 1200 1829" xmlns="http://www.w3.org/2000/svg" aria-hidden="false">
      <defs>
        <clipPath id="frame-inner">
          <g transform="translate(612 640) rotate(-45)">
            <circle cx="0" cy="0" r="272"/>
            <rect x="0" y="-272" width="2200" height="544"/>
          </g>
        </clipPath>
        <linearGradient id="portrait-tone" x1="0" y1="0" x2="0" y2="1">
          <stop offset="0" stop-color="#d9cfb8"/>
          <stop offset="0.22" stop-color="#7a5a4a"/>
          <stop offset="0.45" stop-color="var(--photo-mid)"/>
          <stop offset="1" stop-color="var(--photo-dark)"/>
        </linearGradient>
      </defs>

      <g class="frame-band" transform="translate(612 640) rotate(-45)">
        <circle cx="0" cy="0" r="337" fill="var(--amber)"/>
        <rect x="0" y="-337" width="2200" height="674" fill="var(--amber)"/>
      </g>
      <g class="frame-window" transform="translate(612 640) rotate(-45)">
        <circle cx="0" cy="0" r="272" fill="var(--white)"/>
        <rect x="0" y="-272" width="2200" height="544" fill="var(--white)"/>
      </g>

      <g clip-path="url(#frame-inner)">
        <rect class="author-portrait" role="img"
              aria-label="Photo: the author in a straw boater hat with a striped band, tinted glasses and a grey face mask, wearing a dark jacket"
              x="360" y="150" width="610" height="760" rx="40"
              fill="url(#portrait-tone)"/>
      </g>
    </svg>

    <header class="title-block">
      <h1 class="title-kicker">The Quiet Harbor's</h1>
      <p class="title-main">DRIFT LEDGER</p>
    </header>

    <section class="subtitle">
      <p class="subtitle-count">40 Habits</p>
      <p class="subtitle-line">You Might Shed on the Road to a Calmer Year</p>
      <p class="subtitle-tail">in the Season of <strong>Change</strong></p>
    </section>

    <div class="author-band">
      <p class="author-name">Dr. Marvin T. Okafor</p>
    </div>

    <p class="foreword">Foreword by <span class="foreword-name">Leopold Vantrease,</span> Ph.D.</p>
  </main>
</body>
</html>
```